Grow Stronger With Marla Sunrise Group Workout

We need to launch a grand opening for March of 2016. We offer early morning 6 am to 7 am group exercise.
Two Programs: Mon/Wed/Fri - 3X/week OR Tues/Thurs - 2X/week.
All programs have optional Steadfast Fuel Coaching. Space is limited to 20 persons for each program.
Please use purple and red as two of the colours.
My business name is Grow Stronger With Marla Ltd
I don't know what else I need to supply to create the flyer...I have no experience with this sort of thing. Whatever the .designers come up with that is appropriate for a group fitness workout that will convey people having fun, energetic and uplifting.
This will be an indoor and outdoor group fitness workout.
Pre-registration is required. Come and try a complimentary session.
Contact information:
Trainer: Marla Trevin
Business name: Grow Stronger With Marla Ltd
Certifications: Personal Trainer
Steadfast Fuel Coach level 1
Nutrition & Wellness Specialist
Korvel Bootcamp
Business number: 604-519-3806
email: growstrongerwithmarla@fitmailbox.test
General public, male and female over age of consent
Group
Grow Stronger With Marla
- I'd like to see some pictures, photographs of people of different shapes and sizes generally having fun while doing a group outdoor/indoor workout.

```html
<!DOCTYPE html>
<html lang="en">
<head>
<meta charset="utf-8">
<title>Grow Stronger With Marla – Sunrise Group Workout</title>
<link rel="stylesheet" href="https://fonts.googleapis.com/css2?family=Jost:wght@600;700&family=Oswald:wght@300;400;500&display=swap">
<style>
  :root {
    --red-deep: #8e0a12;
    --red: #d21a22;
    --red-box: #a70d13;
    --purple-deep: #2a0f5e;
    --purple: #5a2ca8;
    --purple-box: #33104f;
    --white: #ffffff;
    --photo-light: #e8f0dc;
    --photo-mid: #9db57a;
  }
  html, body { margin: 0; padding: 0; overflow: hidden; }
  body { width: 779px; height: 1200px; }
  .flyer {
    position: relative;
    width: 779px;
    height: 1200px;
    overflow: hidden;
    color: var(--white);
    font-family: "Jost", sans-serif;
    background:
      radial-gradient(ellipse 420px 360px at 720px 120px, var(--purple) 0%, rgba(90,44,168,0) 70%),
      radial-gradient(ellipse 380px 520px at 120px 250px, #b0121c 0%, rgba(176,18,28,0) 75%),
      radial-gradient(ellipse 500px 400px at 620px 1050px, #e2242c 0%, rgba(226,36,44,0) 75%),
      radial-gradient(ellipse 300px 300px at 60px 1150px, var(--red-deep) 0%, rgba(142,10,18,0) 80%),
      linear-gradient(160deg, var(--red-deep) 0%, #7a1a6a 35%, var(--purple-deep) 55%, var(--red) 80%, var(--red-deep) 100%);
  }
  .tagline {
    position: absolute; left: 35px; top: 34px; width: 720px;
    margin: 0; font-weight: 700; font-size: 25px; line-height: 36px;
    letter-spacing: 0.4px;
  }
  .brand-name {
    position: absolute; left: 0; width: 779px; text-align: center;
    margin: 0; font-weight: 700; color: var(--white); line-height: 1;
  }
  .brand-name--hero { top: 132px; font-size: 52px; }
  .brand-name--hero .line { display: block; }
  .brand-name--hero .line--second { padding-left: 150px; margin-top: 8px; font-size: 44px; }
  .brand-name--footer { top: 1006px; font-size: 34px; }
  .opening {
    position: absolute; left: 35px; top: 212px; margin: 0;
    font-weight: 700; font-size: 17px; line-height: 22px; letter-spacing: 1px;
  }
  .mission {
    position: absolute; left: 147px; top: 256px; width: 625px;
    margin: 0; font-weight: 700; font-size: 25px; line-height: 36px;
  }
  .about-box {
    position: absolute; left: 28px; top: 343px; width: 302px; height: 498px;
    background: var(--purple-box); border: 3px solid var(--white);
  }
  .about-box p {
    margin: 0; padding: 16px 10px 0 11px;
    font-family: "Oswald", sans-serif; font-weight: 300;
    font-size: 22px; line-height: 33.4px; letter-spacing: 0.5px;
  }
  .photo {
    position: absolute; left: 339px; top: 359px; width: 409px; height: 353px;
    border: 2px solid var(--white);
    background: linear-gradient(170deg, var(--photo-light) 0%, var(--photo-mid) 45%, #c9a3b8 75%, #6c6f7a 100%);
  }
  .schedule-box {
    position: absolute; left: 287px; top: 650px; width: 442px; height: 294px;
    background: var(--red-box); border: 3px solid var(--white);
    text-align: center; font-family: "Oswald", sans-serif;
  }
  .schedule-box h2 {
    margin: 16px 0 6px; font-weight: 500; font-size: 25px; line-height: 32px; letter-spacing: 1px;
  }
  .schedule-box .times {
    margin: 0; font-weight: 300; font-size: 23px; line-height: 32px;
  }
  .schedule-box .note {
    margin: 6px 0 0; font-weight: 300; font-size: 21px; line-height: 30px;
  }
  .schedule-box .invite {
    margin: 2px 0 0; font-weight: 400; font-size: 19px; line-height: 28px;
  }
  .care-note {
    position: absolute; left: 29px; top: 866px; margin: 0;
    font-weight: 700; font-size: 20px; line-height: 30px;
  }
  .contact {
    position: absolute; left: 0; top: 1054px; width: 779px; text-align: center;
    font-style: normal; font-weight: 700; font-size: 21px; line-height: 29px;
  }
  .contact p { margin: 0; }
  .contact .phone { font-size: 25px; }
  .contact .credentials { margin-top: 8px; font-weight: 600; font-size: 13px; line-height: 17px; }
  .contact svg { vertical-align: -2px; margin-right: 6px; }
</style>
</head>
<body>
<main class="flyer">
  <p class="tagline">We only have one life to live; our body is our<br>temple.&nbsp; Invest in your temple…invest in yourself.</p>

  <h1 class="brand-name brand-name--hero"><span class="line">Grow Stronger</span><span class="line line--second">With Marla</span></h1>

  <p class="opening">GRAND OPENING<br>MARCH 2016</p>

  <p class="mission">to create a sustainable healthy lifestyle through<br>daily quality nutrition and active living.</p>

  <section class="about-box">
    <p>Marla will work with you to<br>find the nutrition, exercise and<br>stress-management strategies<br>that fit easily in to your life.<br>Helping you to take control of<br>your life and fitness again<br>without unsustainable fads,<br>quick-fixes and confusing<br>advice.&nbsp; Instead we will<br>provide coaching<br>programs using the most-<br>up-to-date health,<br>fitness, nutrition and<br>coaching information.</p>
  </section>

  <div class="photo" role="img" aria-label="Photo of a smiling group of adults stretching their arms overhead during an outdoor workout in a park"></div>

  <section class="schedule-box">
    <h2>EARLY MORNING GROUP EXERCISE</h2>
    <p class="times">6 AM TO 7 AM - Two Programs:<br>Mon/Wed/Fri - 3X/week OR<br>Tues/Thurs - 2X/week.</p>
    <p class="note">All programs have optional Steadfast Fuel<br>Coaching. Space is limited to 20 persons<br>for each program.</p>
    <p class="invite">Pre-registration required. Try a complimentary session!</p>
  </section>

  <p class="care-note">We care about you and<br>your success. We love<br>our temple at Grow<br>Stronger With Marla.&nbsp; Isn't it time you love your temple?</p>

  <p class="brand-name brand-name--footer">Grow Stronger With Marla</p>

  <address class="contact">
    <p>Call or email us FOR RSVP or MORE INFORMATION</p>
    <p><svg width="20" height="15" viewBox="0 0 20 15" aria-hidden="true"><rect x="1" y="1" width="18" height="13" fill="none" stroke="#fff" stroke-width="1.6"/><path d="M1 1 L10 8 L19 1" fill="none" stroke="#fff" stroke-width="1.6"/></svg>growstrongerwithmarla@fitmailbox.test</p>
    <p class="phone"><svg width="20" height="18" viewBox="0 0 20 18" aria-hidden="true"><path d="M2 6 Q10 0 18 6 L16 8 L13 6.5 L13 5 Q10 4 7 5 L7 6.5 L4 8 Z" fill="#fff"/><rect x="4" y="9" width="12" height="8" rx="1.5" fill="#fff"/><circle cx="10" cy="13" r="2" fill="#b0121c"/></svg>604-519-3806</p>
    <p class="credentials">Trainer Marla Trevin · Personal Trainer · Steadfast Fuel Coach level 1<br>Nutrition &amp; Wellness Specialist · Korvel Bootcamp</p>
  </address>
</main>
</body>
</html>
```